Argan Oil Shampoo/Conditioner Label

We are looking for 2 label designs. One for a shampoo bottle, and one for a conditioner bottle. The designs will be similar, however on the conditioner bottle, on the bottom of the label we would like a colored line across acting as a visual indicator to distinguish the two bottles.
Update - Brand name is being finalized but instead of essentials use "Meadow - Concept use a raindrop in place of the apostrophe. And smaller font for “Meadow” directly under “Tem’s”
As for the label, we are looking for a background design for the label as well as some concepts for the main product information and we will need to add the ingredients and instructions later.
Concepts for the Product label, the shampoo and conditioner is going to consist of Argan Oil, so having a black silhouette of an argan tree.
We don’t want something too extravagant or gaudy. Something simple but will make the product look high class. This will be a premium product and we want the label to portray that.
Update- The label dimensions are estimated to be 7.75" wrapped around the bottle. The height of the label will be estimated at 5" from top to bottom.
Please use your artistic minds, we are open to other ideas and concepts as well with keeping to the above mentioned restrictions of not being too gaudy and extravagant.
We are seeking some revisions from a designer and are wanting to give him some more time.

```html
<!DOCTYPE html>
<html lang="en">
<head>
<meta charset="utf-8">
<title>Tem’s Meadow – Shampoo &amp; Conditioner Labels</title>
<link href="https://fonts.googleapis.com/css2?family=Oswald:wght@700&family=Open+Sans:ital,wght@0,400;0,600;1,400&display=swap" rel="stylesheet">
<style>
  :root {
    --page-bg: #dcdcdc;
    --label-bg: #ffffff;
    --ink: #222222;
    --ink-soft: #444444;
    --muted: #c8c8c8;
    --blue: #2aa9e8;
    --gold: #d4a84a;
    --leaf-green: #6c9a47;
    --leaf-olive: #b38b46;
  }
  html, body {
    margin: 0;
    padding: 0;
    width: 1200px;
    height: 1200px;
    overflow: hidden;
    background: var(--page-bg);
    font-family: "Open Sans", Arial, sans-serif;
  }
  .canvas {
    position: relative;
    width: 1200px;
    height: 1200px;
  }
  .label {
    position: absolute;
    top: 160px;
    width: 460px;
    height: 880px;
    background: var(--label-bg);
    box-shadow: 0 2px 10px rgba(0,0,0,0.08);
  }
  .label--shampoo { left: 100px; --accent: var(--blue); }
  .label--conditioner { left: 640px; --accent: var(--gold); }

  .brand {
    position: absolute;
    right: 40px;
    top: 150px;
    margin: 0;
    font-family: "Open Sans", Arial, sans-serif;
    font-weight: 600;
    font-size: 118px;
    line-height: 1;
    color: var(--ink);
    letter-spacing: -2px;
    text-transform: uppercase;
  }
  .sub-brand {
    position: absolute;
    right: 40px;
    top: 300px;
    margin: 0;
    font-weight: 400;
    font-size: 56px;
    line-height: 1;
    color: var(--ink);
    text-transform: uppercase;
    padding-bottom: 8px;
  }
  .sub-brand::after {
    content: "";
    position: absolute;
    left: 6px;
    right: 0;
    bottom: -4px;
    height: 2px;
    background: var(--accent);
  }
  .tagline {
    position: absolute;
    right: 40px;
    top: 380px;
    margin: 0;
    font-size: 11px;
    line-height: 1.5;
    color: var(--ink-soft);
    text-align: right;
  }
  .product-type {
    position: absolute;
    right: 54px;
    top: 470px;
    height: 200px;
    display: flex;
    gap: 2px;
    writing-mode: vertical-rl;
    transform: rotate(180deg);
    justify-content: flex-start;
  }
  .product-type__name {
    font-style: italic;
    font-size: 25px;
    letter-spacing: 1px;
    color: var(--accent);
    text-transform: uppercase;
  }
  .product-type__note {
    font-style: italic;
    font-size: 12px;
    color: var(--muted);
    text-transform: uppercase;
    letter-spacing: 1px;
  }
  .argan-branch {
    position: absolute;
    left: 10px;
    top: 500px;
    width: 160px;
    height: 300px;
    border-radius: 80px 20px 80px 20px;
    background: linear-gradient(160deg, var(--leaf-green), var(--leaf-olive) 60%, var(--leaf-green));
    opacity: 0.85;
  }
  .hair-type {
    position: absolute;
    right: 40px;
    top: 690px;
    width: 160px;
    text-align: right;
  }
  .hair-type__icon {
    position: absolute;
    left: -14px;
    top: 0;
  }
  .hair-type__title {
    margin: 0;
    font-size: 13px;
    font-weight: 600;
    color: var(--ink);
    padding-bottom: 4px;
    border-bottom: 2px solid var(--accent);
  }
  .hair-type__text {
    margin: 6px 0 0;
    font-size: 11px;
    line-height: 1.4;
    color: var(--ink-soft);
  }
  .formula-band {
    position: absolute;
    right: 40px;
    top: 775px;
    width: 240px;
    height: 30px;
    border-radius: 0 15px 15px 0;
    background: var(--accent);
    color: var(--ink);
    font-size: 14px;
    line-height: 30px;
    text-align: right;
    padding-right: 10px;
    box-sizing: border-box;
  }
  .volume {
    position: absolute;
    right: 40px;
    top: 838px;
    margin: 0;
    font-size: 12px;
    font-weight: 600;
    color: var(--ink);
  }
</style>
</head>
<body>
<main class="canvas">

  <section class="label label--shampoo">
    <h1 class="brand">Tem’s</h1>
    <h2 class="sub-brand">Meadow</h2>
    <p class="tagline">Enriced with natural Argan Oil,<br>Powerful blend of essential herbs.</p>
    <div class="product-type">
      <span class="product-type__name">Shampoo</span>
      <span class="product-type__note">(Organic)</span>
    </div>
    <div class="argan-branch" role="img" aria-label="Illustrated argan branch with green leaves and golden argan fruits"></div>
    <div class="hair-type">
      <svg class="hair-type__icon" width="16" height="44" viewBox="0 0 16 44" aria-hidden="true">
        <path d="M12 2 Q4 14 8 34" fill="none" stroke="var(--blue)" stroke-width="1.5"/>
        <circle cx="8" cy="37" r="5" fill="none" stroke="var(--blue)" stroke-width="1.5"/>
        <circle cx="8" cy="37" r="2" fill="var(--blue)"/>
      </svg>
      <p class="hair-type__title">FOR ALL HAIR TYPE</p>
      <p class="hair-type__text">Every one deserves to<br>look &amp; feel fabulous</p>
    </div>
    <div class="formula-band">Quick hair restoration formula</div>
    <p class="volume">500ML</p>
  </section>

  <section class="label label--conditioner">
    <h1 class="brand">Tem’s</h1>
    <h2 class="sub-brand">Meadow</h2>
    <p class="tagline">Enriced with natural Argan Oil,<br>Powerful blend of essential herbs.</p>
    <div class="product-type">
      <span class="product-type__name">Conditioner</span>
      <span class="product-type__note">(Organic)</span>
    </div>
    <div class="argan-branch" role="img" aria-label="Illustrated argan branch with green leaves and golden argan fruits"></div>
    <div class="hair-type">
      <svg class="hair-type__icon" width="16" height="44" viewBox="0 0 16 44" aria-hidden="true">
        <path d="M12 2 Q4 14 8 34" fill="none" stroke="var(--gold)" stroke-width="1.5"/>
        <circle cx="8" cy="37" r="5" fill="none" stroke="var(--gold)" stroke-width="1.5"/>
        <circle cx="8" cy="37" r="2" fill="var(--gold)"/>
      </svg>
      <p class="hair-type__title">FOR ALL HAIR TYPE</p>
      <p class="hair-type__text">Every one deserves to<br>look &amp; feel fabulous</p>
    </div>
    <div class="formula-band">Quick hair restoration formula</div>
    <p class="volume">500ML</p>
  </section>

</main>
</body>
</html>
```